THE HEADLAND AT TALL PINE HUDSON RIVER WATERFRONT LAND

crisp clear business cards on wood stock or thick paper with large font with a river otter logo, PERSONAL INFO ON ONE SIDE, PROJECT INFO ON THE OTHER SIDE
Updates

I don’t have a logo. Just thought that a photo of a river otter would look appealing.

Target Market(s)

Buyers and realtors

Industry/Entity Type

Real Estate Development

Contact Information for Business Card

MARTIN KOWALCZYK
607-318-5942 (Call or Text)
STONE MEADOW LLC PRINCIPAL

RQVWFIELD@NORVAMAIL.NET

Font styles to use
Sans Serif

Colors
fbfdfe
0792cd
00a990
fbed22
ec1f27

Requirements
Must have
• LARGE FONT, ROUNDED EDGES,
Nice to have
• ON THE BACK SIDE :
• THE HEADLAND AT TALL PINE
• HUDSON RIVER WATERFRONT LAND
• 2 TO 67 ACRES---READY TO BUILD
• PRICED TO SELL!

```html
<!DOCTYPE html>
<html lang="en">
<head>
<meta charset="utf-8">
<title>Stone Meadow LLC – Business Card</title>
<link rel="stylesheet" href="https://fonts.googleapis.com/css2?family=Lato:wght@400;700&display=swap">
<style>
  :root {
    --backdrop: #e6e8ea;
    --paper: #fbfdfe;
    --blue: #0792cd;
    --teal: #00a990;
    --ink: #1b1b1b;
    --rule: #a3a3a3;
    --shadow: rgba(0, 0, 0, 0.18);
  }
  * { box-sizing: border-box; margin: 0; padding: 0; }
  html, body {
    width: 1200px;
    height: 782px;
    overflow: hidden;
    background: var(--backdrop);
    font-family: "Lato", "Helvetica Neue", Arial, sans-serif;
  }
  .canvas {
    width: 1200px;
    height: 782px;
    display: flex;
    align-items: center;
    justify-content: center;
    gap: 40px;
  }
  .card {
    width: 520px;
    height: 297px;
    border-radius: 22px;
    box-shadow: 0 10px 24px var(--shadow);
    overflow: hidden;
    display: flex;
    flex-direction: column;
    align-items: center;
  }

  /* Front: gradient, company name and project info */
  .card--front {
    background: linear-gradient(205deg, var(--teal) 0%, var(--blue) 45%, var(--blue) 60%, var(--teal) 100%);
    color: var(--paper);
    justify-content: center;
    text-align: center;
  }
  .brand-dot {
    width: 46px;
    height: 46px;
    border-radius: 50%;
    background: var(--paper);
  }
  .brand-name {
    font-weight: 700;
    font-size: 28px;
    letter-spacing: 2px;
    line-height: 1;
    margin-top: 14px;
  }
  .brand-rule {
    width: 300px;
    height: 1.5px;
    background: var(--paper);
    opacity: 0.85;
    margin: 14px 0 14px;
  }
  .project-name {
    font-weight: 700;
    font-size: 19px;
    letter-spacing: 1px;
    line-height: 1.2;
  }
  .project-detail {
    font-size: 15px;
    letter-spacing: 1px;
    line-height: 1.35;
    margin-top: 3px;
  }

  /* Back: contact details */
  .card--back {
    background: var(--paper);
    padding-top: 44px;
  }
  .company {
    color: var(--blue);
    font-weight: 700;
    font-size: 34px;
    letter-spacing: 1.5px;
    line-height: 1;
  }
  .company-rule {
    width: 360px;
    height: 2px;
    background: var(--rule);
    margin-top: 14px;
  }
  .contact {
    margin-top: 22px;
    text-align: center;
  }
  .person {
    font-weight: 700;
    font-size: 22px;
    letter-spacing: 0.5px;
    line-height: 1.1;
  }
  .person__first { color: var(--blue); }
  .person__last { color: var(--teal); }
  .role {
    color: var(--ink);
    font-size: 13px;
    letter-spacing: 1px;
    margin-top: 2px;
  }
  .contact-rule {
    width: 240px;
    height: 1.5px;
    background: var(--rule);
    margin: 10px auto;
  }
  .phone {
    font-size: 18px;
    color: var(--ink);
  }
  .phone__call { color: var(--blue); }
  .phone__text { color: var(--teal); }
  .email {
    font-size: 14px;
    color: var(--ink);
    letter-spacing: 0.5px;
    margin-top: 4px;
  }
</style>
</head>
<body>
  <main class="canvas">
    <section class="card card--front" aria-label="Card front">
      <span class="brand-dot" aria-hidden="true"></span>
      <p class="brand-name">STONE MEADOW LLC</p>
      <div class="brand-rule"></div>
      <p class="project-name">THE HEADLAND AT TALL PINE</p>
      <p class="project-detail">HUDSON RIVER WATERFRONT LAND</p>
      <p class="project-detail">2 TO 67 ACRES — READY TO BUILD</p>
    </section>

    <section class="card card--back" aria-label="Card back">
      <h1 class="company">STONE MEADOW LLC</h1>
      <div class="company-rule"></div>
      <div class="contact">
        <p class="person"><span class="person__first">MARTIN</span> <span class="person__last">KOWALCZYK</span></p>
        <p class="role">PRINCIPAL</p>
        <div class="contact-rule"></div>
        <p class="phone"><span class="phone__call">Call</span> or <span class="phone__text">Text</span> : 607-318-5942</p>
        <p class="email">RQVWFIELD@NORVAMAIL.NET</p>
      </div>
    </section>
  </main>
</body>
</html>
```